Psychologist in Private Practice Needs a Website Update

Project Description:
Hello talented designers! My current website, www.jodelbrisk.com, needs a fresh, boho-modern makeover that highlights the warm, welcoming nature of my holistic therapy practice. I want a website that has a serene, boho- modern design, appealing to clients seeking individual therapy, couples therapy, and family counseling.

I’d also like to prepare for a future second site focused exclusively on couples and family therapy. Both sites should be interconnected, so I’m looking for design suggestions that seamlessly link them together while maintaining a cohesive brand look and feel.

Key Objectives:

Boho-Modern Aesthetic: Incorporate natural textures, neutral or earthy tones, and clean lines that capture a modern, inviting vibe.

Responsive Design: Ensure the website is user-friendly on desktop, tablet, and mobile devices.

Clear Service Offerings: Prominently feature my three distinct services: individual therapy, couples therapy, and family counseling.

Interlinked Future Site: Provide ideas on how to cross-link this site with a second site focused on couples and family therapy.

User Experience (UX): Make the site simple to navigate, with intuitive placement of content that speaks to potential clients’ needs.

SEO-Friendly: Implement best practices for structure, site speed, and keyword usage to boost online visibility.

What I Have Now:
Existing website: www.jodelbrisk.com
Basic content and a logo that can be refined or updated to match the boho-modern feel
Rough style guide with brand elements open to a fresh interpretation

Preferred Style/Tone:
Boho-modern with earthy tones, subtle textures, and clean typography
Warm, empathetic, and approachable to align with the nature of therapy services
Slightly artistic or organic elements that evoke calm and connection

Potential for an ongoing design relationship!
Updates

Need extra days to review

Target Market(s)

I have a high functioning, professional clientele who doctors, lawyers, and leaders in their field.

Industry/Entity Type

healthcare/mental health

Coding

Coded - Design and coding required

Font styles to use
Other font styles liked:
• cormorant garamond for headers and Source Sans Pro for supporting text

Colors

Designer to choose colors to be used in the design.

Requirements
Must have
• Open, Harmonious Layout I’d like the overall design to feel upscale, humanistic, open and harmonious, with minimal divisions of space. Rather than traditional section dividers, please consider using images, subtle shifts in color, typography, or spacing to define sections. Hero Image & Inspiration Ideally, the first (hero) image should evoke a sense of awe or inspiration. Focus on simplicity and elegance so the design feels spacious and inviting, allowing the content and imagery to really stand out. Natural Flow Wherever possible, let the design elements flow naturally into each other, creating a sense of unity and cohesion throughout the site.
Nice to have
• 1. Full-Width Hero Image: • The homepage should feature a full-width hero image that extends edge-to-edge across the screen for a modern and visually immersive effect. • This image should set the tone for the website, reflecting a calming, humanistic/natural, and upscale feel. It could include subtle overlays or gradients to enhance readability of text and navigation elements. Ideally, this image should have one or two people in nature. The image could be slightly transparent to allow the text "holistic therapy" and the tagline "an integrative approach to transformation" to be easily visible. Please help me find a breath-taking image that evokes a sense of beauty, inspiration, awe or hope. 2. Menu Tabs Positioned Over the Image: • The menu tabs (navigation bar) should be positioned directly on top of the hero image, either centered or aligned to the top right/left, depending on the design. • The navigation bar should have a slightly transparent or solid background (depending on the image and visibility needs) to ensure the text is easily readable without detracting from the image. 3. Typography and Text Placement: • The text overlay on the hero image should use the selected fonts: • Cormorant Garamond for headers (e.g., the tagline or welcome message). • Source Sans Pro for any supporting text. 5. Seamless Transitions: • Below the full-width image, transitions into the next sections (like “About,” “Services,” or client-focused content) should be smooth, using full-width separators that maintain the cohesive, open layout style. 6. Color Palette: • A neutral and calming color palette should be used (e.g., soft blues, grays, whites, or very muted earth tones) to create a soothing atmosphere for visitors. This design approach ensures the homepage looks clean, modern, and professional while maintaining the calming and upscale aesthetic that reflects the values of my psychology practice

```html
<!DOCTYPE html>
<html lang="en">
<head>
<meta charset="utf-8">
<title>Dr. Jodel Brisk — Licensed Psychologist</title>
<link href="https://fonts.googleapis.com/css2?family=Poppins:wght@300;400;500;600;700&display=swap" rel="stylesheet">
<style>
:root{
  --blush:#e0cfc9;
  --card:#dcc9c1;
  --linen:#ece8e2;
  --ink:#161616;
  --accent:#b98e7d;
  --gold:#e9b23b;
  --dark:#1d1d1d;
  --photo-warm:#a88366;
  --photo-deep:#4c3f34;
  --white:#ffffff;
}
*{margin:0;padding:0;box-sizing:border-box}
html,body{width:1200px;height:3565px;overflow:hidden;background:var(--linen)}
body{font-family:'Poppins',sans-serif;color:var(--ink)}
.page{position:relative;width:1200px;height:3565px;background:var(--linen);overflow:hidden}
.abs{position:absolute}
.band-top{left:0;top:0;width:1200px;height:598px;background:var(--blush)}
.band-mid{left:0;top:2535px;width:1200px;height:748px;background:var(--blush)}
.brand{left:154px;top:18px;line-height:1.1}
.brand .name{font-size:25px;font-weight:400}
.brand .role{font-size:17px;font-weight:400}
.nav{top:36px;font-size:14.5px;font-weight:400;white-space:nowrap}
.nav span{position:absolute;transform:translateX(-50%)}
.caret{display:inline-block;width:6px;height:6px;border-right:1.2px solid currentColor;border-bottom:1.2px solid currentColor;transform:rotate(45deg);margin-left:5px;vertical-align:3px}
.signature{left:42px;top:118px;width:62px;height:394px;background:rgba(40,30,25,.08);border-radius:30px}
.side-line{left:68px;top:542px;width:2px;height:708px;background:var(--ink)}
.arch{border-radius:215px 215px 0 0;overflow:hidden}
.hero-photo{left:154px;top:101px;width:430px;height:568px;background:linear-gradient(180deg,#fbfaf9 0%,#e9d8ca 30%,var(--photo-warm) 70%,#5a4a42 100%)}
.hero-title{left:628px;top:275px;font-size:52px;font-weight:400;letter-spacing:.5px}
.hero-sub{left:628px;top:344px;font-size:20.5px;font-weight:400}
.btn{display:flex;align-items:center;justify-content:center;background:var(--white);font-size:14.5px;color:var(--ink)}
.struggle{left:154px;top:876px;width:460px}
.struggle h2{font-size:29px;line-height:45px;font-weight:400}
.struggle h2 b{font-weight:700}
.struggle p{margin-top:12px;font-size:13.3px;line-height:23px}
.checks{list-style:none;margin-top:24px}
.checks li{display:flex;align-items:center;gap:10px;font-size:13px;font-weight:600;height:25.6px}
.photo-couple{left:639px;top:754px;width:431px;height:568px;background:linear-gradient(180deg,#5f7052 0%,#bfd0d3 35%,#b26e5a 52%,#6f8aa7 70%,#3c3d40 100%)}
.intro{left:150px;top:1368px;width:900px;text-align:center;font-size:13.3px;line-height:23px}
.intro p+p{margin-top:23px}
.section-title{width:1200px;left:0;text-align:center;font-size:29px;font-weight:400}
.section-title b{font-weight:700}
.service{top:1611px;width:278px;height:364px;border-radius:139px;background:var(--card);text-align:center}
.service svg.icon{position:absolute;left:104px;top:74px}
.service h3{position:absolute;top:172px;width:100%;font-size:22px;font-weight:500}
.service p{position:absolute;top:212px;left:14px;right:14px;font-size:13.3px;line-height:23px}
.service .plus{position:absolute;left:128px;top:302px}
.partner-photo{left:154px;top:2155px;width:430px;height:566px;background:linear-gradient(180deg,#3e342b 0%,#56463a 40%,#a0744e 70%,#6d5848 100%)}
.partner-sign{left:462px;top:2280px;width:50px;height:400px;background:rgba(255,255,255,.12);border-radius:25px}
.partner{left:628px;top:2220px;width:445px}
.partner h2{font-size:29px;font-weight:400}
.partner h2 b{font-weight:700}
.partner p{margin-top:14px;font-size:13.3px;line-height:23px}
.blog-card{top:2872px;width:289px;height:331px;background:var(--white);border-radius:6px;overflow:hidden}
.blog-card .img{height:173px}
.blog-card .date{position:absolute;left:0;top:173px;width:44px;height:47px;background:var(--gold);color:var(--white);text-align:center;line-height:1}
.blog-card .date b{display:block;font-size:19px;font-weight:500;padding-top:5px}
.blog-card .date span{font-size:15px}
.blog-card h4{position:absolute;left:54px;top:182px;width:225px;font-size:14px;font-weight:500;line-height:21px}
.blog-card p{position:absolute;left:54px;top:226px;width:232px;font-size:11.3px;line-height:20px}
.blog-card a{position:absolute;left:54px;top:296px;font-size:11px;color:var(--gold);text-decoration:underline}
.arrow{width:31px;height:31px;border-radius:50%;background:var(--white);top:3023px;display:flex;align-items:center;justify-content:center}
.footer{left:0;top:3283px;width:1200px;height:282px;background:var(--dark);color:var(--white)}
.footer .nav{top:44px;font-size:14.5px}
.footer .rule{position:absolute;left:147px;top:105px;width:926px;height:1px;background:#3a3a3a}
.contact{top:135px;display:flex;align-items:center;gap:12px}
.contact .label{font-size:11px;font-weight:600;line-height:1.3}
.contact .value{font-size:13px;line-height:1.4}
.contact .big{font-size:22px;line-height:1.2}
.vsep{top:145px;width:1px;height:32px;background:#555}
.copy{left:147px;top:246px;font-size:11.5px}
.social{top:250px;width:8px;height:8px;border-radius:50%;background:var(--white)}
</style>
</head>
<body>
<div class="page">

  <div class="abs band-top"></div>
  <div class="abs band-mid"></div>

  <header>
    <div class="abs brand"><div class="name">Dr. Jodel Brisk</div><div class="role">Licensed Psychologist</div></div>
    <nav class="abs nav" style="left:0;width:1200px">
      <span style="left:543px">Welcome</span>
      <span style="left:662px">Services<i class="caret"></i></span>
      <span style="left:770px">About</span>
      <span style="left:861px">FAQ's</span>
      <span style="left:947px">Blog</span>
      <span style="left:1052px">FAQ's</span>
    </nav>
  </header>

  <div class="abs signature" role="img" aria-label="Hand-lettered signature of Dr. Jodel Brisk, set vertically"></div>
  <div class="abs side-line"></div>

  <section class="hero">
    <div class="abs arch hero-photo" role="img" aria-label="Portrait of Dr. Jodel Brisk on a white background"></div>
    <h1 class="abs hero-title">Holistic Therapy</h1>
    <p class="abs hero-sub">An Integrative Approach To Transformation</p>
    <a class="abs btn" style="left:628px;top:396px;width:130px;height:48px">Read More</a>
  </section>

  <section>
    <div class="abs struggle">
      <h2>Are You Struggling With Issues<br><b>That Affect The Way You Live,<br>Love Or Work?</b></h2>
      <p>Dr. Jodel Brisk and her associates are licensed psychologists in Alder Grove, Maryland. We offer therapy for individuals, couples and families to help you create meaningful change, whether you:</p>
      <ul class="checks">
        <li><svg width="15" height="15" viewBox="0 0 15 15"><rect x="1" y="2" width="11" height="11" fill="none" stroke="#e9b23b" stroke-width="1.6"/><path d="M4 7l3 3 7-8" fill="none" stroke="#e9b23b" stroke-width="2"/></svg>Feel overwhelmed with depression or anxiety.</li>
        <li><svg width="15" height="15" viewBox="0 0 15 15"><rect x="1" y="2" width="11" height="11" fill="none" stroke="#e9b23b" stroke-width="1.6"/><path d="M4 7l3 3 7-8" fill="none" stroke="#e9b23b" stroke-width="2"/></svg>Experience a lack of connection in your marriage.</li>
        <li><svg width="15" height="15" viewBox="0 0 15 15"><rect x="1" y="2" width="11" height="11" fill="none" stroke="#e9b23b" stroke-width="1.6"/><path d="M4 7l3 3 7-8" fill="none" stroke="#e9b23b" stroke-width="2"/></svg>Worry excessively about what others think.</li>
        <li><svg width="15" height="15" viewBox="0 0 15 15"><rect x="1" y="2" width="11" height="11" fill="none" stroke="#e9b23b" stroke-width="1.6"/><path d="M4 7l3 3 7-8" fill="none" stroke="#e9b23b" stroke-width="2"/></svg>Have a history of trauma or abuse.</li>
        <li><svg width="15" height="15" viewBox="0 0 15 15"><rect x="1" y="2" width="11" height="11" fill="none" stroke="#e9b23b" stroke-width="1.6"/><path d="M4 7l3 3 7-8" fill="none" stroke="#e9b23b" stroke-width="2"/></svg>Parent a child with complex needs.</li>
        <li><svg width="15" height="15" viewBox="0 0 15 15"><rect x="1" y="2" width="11" height="11" fill="none" stroke="#e9b23b" stroke-width="1.6"/><path d="M4 7l3 3 7-8" fill="none" stroke="#e9b23b" stroke-width="2"/></svg>Struggle with other life challenges.</li>
      </ul>
    </div>
    <div class="abs arch photo-couple" role="img" aria-label="Young couple talking on an ironwork bench outdoors"></div>
  </section>

  <section class="abs intro">
    <p>We have extensive experience treating a full spectrum of mental health disorders using a collaborative and compassionate approach. In addition to individual therapy, we also provide couples counseling and family therapy.</p>
    <p>Dr. Brisk's practice, based in the West Alder Grove area of Linden Bay, is best suited for those who wish to deeply examine their inner world to gain insight, identify what matters most, and create lasting change towards a more fulfilling life.</p>
  </section>

  <section>
    <h2 class="abs section-title" style="top:1540px">Our <b>Services</b></h2>

    <article class="abs service" style="left:154px">
      <svg class="icon" width="70" height="70" viewBox="0 0 70 70" fill="none" stroke="#b98e7d" stroke-width="2"><circle cx="14" cy="26" r="6"/><circle cx="56" cy="26" r="6"/><path d="M4 50v-10a8 8 0 0116 0v10h8M66 50v-10a8 8 0 00-16 0v10h-8M8 50v14M62 50v14"/><rect x="22" y="4" width="18" height="12" rx="6"/><rect x="34" y="10" width="18" height="12" rx="6"/></svg>
      <h3>Individual Therapy</h3>
      <p>Lorem ipsum dolor sit amet, consectetuer adipiscing elit, sed diam laoreet dolore&nbsp; erat volutpat.</p>
      <svg class="plus" width="22" height="22" viewBox="0 0 22 22"><path d="M11 2v18M2 11h18" stroke="#fff" stroke-width="4"/></svg>
    </article>

    <article class="abs service" style="left:472px">
      <svg class="icon" width="70" height="70" viewBox="0 0 70 70" fill="none" stroke="#b98e7d" stroke-width="2"><rect x="10" y="2" width="20" height="13" rx="6"/><rect x="40" y="2" width="20" height="13" rx="6"/><circle cx="20" cy="32" r="8"/><circle cx="50" cy="32" r="8"/><path d="M4 68V54a8 8 0 018-8h16a8 8 0 018 8v14M34 68V54a8 8 0 018-8h16a8 8 0 018 8v14"/></svg>
      <h3>Couples Therapy</h3>
      <p>Lorem ipsum dolor sit amet, consectetuer adipiscing elit, sed diam laoreet dolore&nbsp; erat volutpat.</p>
      <svg class="plus" width="22" height="22" viewBox="0 0 22 22"><path d="M11 2v18M2 11h18" stroke="#fff" stroke-width="4"/></svg>
    </article>

    <article class="abs service" style="left:792px">
      <svg class="icon" width="70" height="70" viewBox="0 0 70 70" fill="none" stroke="#b98e7d" stroke-width="2"><circle cx="18" cy="16" r="10"/><circle cx="52" cy="18" r="10"/><circle cx="35" cy="38" r="8"/><path d="M2 60V44a10 10 0 0110-10h10M68 60V46a10 10 0 00-10-10h-10M22 68v-8a8 8 0 018-8h10a8 8 0 018 8v8"/></svg>
      <h3>Family Counseling</h3>
      <p>Lorem ipsum dolor sit amet, consectetuer adipiscing elit, sed diam laoreet dolore&nbsp; erat volutpat.</p>
      <svg class="plus" width="22" height="22" viewBox="0 0 22 22"><path d="M11 2v18M2 11h18" stroke="#fff" stroke-width="4"/></svg>
    </article>

    <a class="abs btn" style="left:536px;top:2023px;width:128px;height:49px">View All</a>
  </section>

  <section>
    <div class="abs arch partner-photo" role="img" aria-label="Portrait of Dr. Jodel Brisk against a dark backdrop"></div>
    <div class="abs partner-sign" role="img" aria-label="Hand-lettered signature of Dr. Jodel Brisk in white"></div>
    <div class="abs partner">
      <h2>Therapy is a <b>Partnership.</b></h2>
      <p>Our clinicians utilize contemporary neuroscience-informed therapies along with the wisdom of traditional psychotherapy to foster insight, mindfulness, self-compassion, and deeper connections to oneself and others. Together, in a safe and non-judgmental environment, we will work to understand what holds you back from living the life you really want. All are welcome and celebrated.</p>
    </div>
    <a class="abs btn" style="left:627px;top:2433px;width:200px;height:48px">Make An Appointment</a>
  </section>

  <section>
    <h2 class="abs section-title" style="top:2790px">Latest <b>Blog</b></h2>

    <div class="abs arrow" style="left:102px"><svg width="12" height="12" viewBox="0 0 12 12"><path d="M8 1L3 6l5 5" fill="none" stroke="#888" stroke-width="1.4"/></svg></div>
    <div class="abs arrow" style="left:1093px"><svg width="12" height="12" viewBox="0 0 12 12"><path d="M4 1l5 5-5 5" fill="none" stroke="#888" stroke-width="1.4"/></svg></div>

    <article class="abs blog-card" style="left:154px">
      <div class="img" role="img" aria-label="Therapist taking notes during a session with a client" style="background:linear-gradient(135deg,#e8e8e6,#b9bcbd 55%,#4b5560)"></div>
      <div class="date"><b>13</b><span>Jan</span></div>
      <h4>Duis Autem Vel Eum Iriure Dolor In Hendrerit.</h4>
      <p>Lorem ipsum dolor sit amet, consectetuer adipiscing elit, sed diam nonummy nibh euismod tincidunt.</p>
      <a>Read More</a>
    </article>

    <article class="abs blog-card" style="left:469px">
      <div class="img" role="img" aria-label="Client speaking with a counselor holding a notebook" style="background:linear-gradient(135deg,#5a5c5e,#8e9aa8 50%,#c8b6a4)"></div>
      <div class="date"><b>13</b><span>Jan</span></div>
      <h4>Duis autem vel eum iriure dolor in hendrerit.</h4>
      <p>Lorem ipsum dolor sit amet, consectetuer adipiscing elit, sed diam nonummy nibh euismod tincidunt.</p>
      <a>Read More</a>
    </article>

    <article class="abs blog-card" style="left:783px">
      <div class="img" role="img" aria-label="Counselor gesturing while talking with a client by a window" style="background:linear-gradient(135deg,#4a4440,#d8d6d2 55%,#f0eeea)"></div>
      <div class="date"><b>13</b><span>Jan</span></div>
      <h4>Duis autem vel eum iriure dolor in hendrerit.</h4>
      <p>Lorem ipsum dolor sit amet, consectetuer adipiscing elit, sed diam nonummy nibh euismod tincidunt.</p>
      <a>Read More</a>
    </article>
  </section>

  <footer class="abs footer">
    <nav class="abs nav" style="left:0;width:1200px">
      <span style="left:353px">Welcome</span>
      <span style="left:466px">Services<i class="caret"></i></span>
      <span style="left:580px">About</span>
      <span style="left:671px">FAQ's</span>
      <span style="left:757px">Blog</span>
      <span style="left:862px">FAQ's</span>
    </nav>
    <div class="rule"></div>

    <div class="abs contact" style="left:147px">
      <svg width="38" height="38" viewBox="0 0 38 38" fill="none" stroke="#fff" stroke-width="2"><circle cx="19" cy="19" r="17"/><path d="M13 11l3 0 2 5-2 2a11 11 0 005 5l2-2 5 2v3c0 1-1 2-2 2A16 16 0 0111 13c0-1 1-2 2-2z" stroke-width="1.6"/></svg>
      <div><div class="label">CALL US:</div><div class="big">(555) 014-2290</div></div>
    </div>
    <div class="abs vsep" style="left:419px"></div>

    <div class="abs contact" style="left:472px">
      <svg width="38" height="38" viewBox="0 0 38 38" fill="none" stroke="#fff" stroke-width="2"><circle cx="19" cy="19" r="17"/><rect x="11" y="13" width="16" height="12" rx="1" fill="#fff" stroke="none"/><path d="M11 14l8 6 8-6" stroke="#1d1d1d" stroke-width="1.6"/></svg>
      <div><div class="label">EMAIL:</div><div class="value">drjodelbrisk@fernmail.com</div></div>
    </div>
    <div class="abs vsep" style="left:752px"></div>

    <div class="abs contact" style="left:803px">
      <svg width="38" height="38" viewBox="0 0 38 38" fill="none" stroke="#fff" stroke-width="2"><circle cx="19" cy="19" r="17"/><path d="M19 29s-7-7-7-12a7 7 0 0114 0c0 5-7 12-7 12z"/><circle cx="19" cy="17" r="2.5"/></svg>
      <div><div class="label">ADDRESS:</div><div class="value">Lorem ipsum dolor sit amet,<br>consectetur adipiscing elit 1250</div></div>
    </div>

    <div class="abs copy">© 2025&nbsp; Jodel R. Brisk, Psy.D. All Rights Reserved.</div>
    <div class="abs social" style="left:952px" aria-label="Social link"></div>
    <div class="abs social" style="left:986px" aria-label="Social link"></div>
    <div class="abs social" style="left:1022px" aria-label="Social link"></div>
    <div class="abs social" style="left:1058px" aria-label="Social link"></div>
  </footer>

</div>
</body>
</html>
```